Tallow Bodyweight Gym Website

We need a website design for our gym.

Tallow is the UAE's first calisthenics and parkour gym. The theme under which the gym revolves is that one does not require any machinery to workout as our bodies could be themselves the machinery. The gym is designed to be the more of a social hub rather than an "in-and-out" gym, where people come train, have fun, hang out and socialize for a few hours rather than just train for 60 minutes then leave. The gym is designed to be a big open space with lots of natural sunlight, natural wood and plants all over the place to create a natural and refreshing setting. We also use recycled material throughout the gym and recycle our waste as being green is part of our philosophy. We currently also have some of the world's top and most recognized calisthenics athletes working with us.

We would like our website to reflect all that as well as provide a simple, interactive and fun way for visitors to be able to get class and gym information, check out gym media and contact us for bookings.

Target Market(s)

Ages 15-35

Industry/Entity Type

Fitness

Coding

Coded - Design and coding required

Number of Pages Required

4 page

Font styles to use
Decorative

Colors
0792cd

Requirements
Must have
• Class descriptions
• Gym description
• Class schedules
• Trainer profiles
• Gym philosophy
• Contact Details
Nice to have
• A link to contact us directly for a free first trial class

```html
<!DOCTYPE html>
<html lang="en">
<head>
<meta charset="utf-8">
<title>Tallow Bodyweight Gym</title>
<link href="https://fonts.googleapis.com/css2?family=Montserrat:wght@400;500;700&display=swap" rel="stylesheet">
<style>
:root{
  --brand:#0792cd;
  --brand-deep:#0a5e8c;
  --brand-light:#2aa6e0;
  --green:#3fad25;
  --white:#ffffff;
  --line:rgba(255,255,255,.35);
}
*{box-sizing:border-box;margin:0;padding:0}
html,body{width:1200px;height:592px;overflow:hidden}
body{font-family:"Montserrat",sans-serif;color:var(--white);background:var(--brand)}
.page{position:relative;width:1200px;height:592px;overflow:hidden}
.hero-photo{position:absolute;inset:0;background:radial-gradient(ellipse at 55% 45%,#1c9bd6 0%,var(--brand) 45%,#0a86c2 100%)}
.logo{position:absolute;left:176px;top:60px;display:flex;align-items:center;gap:8px}
.logo-dot{width:14px;height:14px;border-radius:50%;background:var(--white)}
.logo-name{font-size:24px;font-weight:700;line-height:1}
.trial{position:absolute;left:720px;top:38px;font-size:18px;font-weight:400}
.contact-btn{position:absolute;left:908px;top:33px;width:117px;height:35px;border:2px solid var(--white);border-radius:18px;display:flex;align-items:center;justify-content:center;font-size:11px;font-weight:700;color:var(--white);text-decoration:none}
.nav{position:absolute;top:100px;left:351px;right:174px;display:flex;justify-content:space-between;list-style:none}
.nav a{color:var(--white);text-decoration:none;font-size:12.5px;font-weight:700;display:block;padding-bottom:4px;border-bottom:1px solid var(--line)}
.intro{position:absolute;right:172px;top:171px;width:590px;text-align:right;font-size:16px;line-height:21px;font-weight:400}
.intro strong{font-weight:700}
.pill{position:absolute;top:290px;height:103px;border-radius:52px;display:flex;align-items:center}
.pill-eco{left:172px;width:441px;background:var(--green)}
.pill-body{left:643px;width:385px;background:var(--brand-deep)}
.pill svg{flex:none}
.pill-eco svg{margin-left:32px;margin-right:34px}
.pill-body svg{margin-left:30px;margin-right:28px}
.pill h2{font-weight:500;text-transform:uppercase}
.pill-eco h2{font-size:23px;margin-bottom:10px}
.pill-body h2{font-size:16.5px;line-height:21px;margin-bottom:10px}
.pill p{font-size:11.5px;line-height:15px}
.feature{position:absolute;top:438px;display:flex;align-items:center;gap:18px;font-size:13px;line-height:17px}
.feature-rank{left:172px}
.feature-social{left:589px}
.divider{position:absolute;left:0;right:0;top:522px;border-top:1px solid var(--line)}
.footer{position:absolute;top:543px;left:172px;right:172px;font-size:11px;line-height:14px}
.copyright{position:absolute;left:0;top:0}
.address{position:absolute;left:201px;top:0;display:flex;gap:8px}
.social{position:absolute;right:0;top:6px;display:flex;gap:22px;list-style:none}
.social li{width:18px;height:18px;border-radius:50%;background:var(--white)}
</style>
</head>
<body>
<div class="page">
  <div class="hero-photo" role="img" aria-label="Blue-tinted photo of an athlete training on bars inside the gym"></div>

  <div class="logo"><span class="logo-dot"></span><span class="logo-name">Tallow</span></div>

  <p class="trial">Try a free trial lesson!</p>
  <a class="contact-btn" href="#">CONTACT US</a>

  <ul class="nav">
    <li><a href="#">CLASS DESCRIPTIONS</a></li>
    <li><a href="#">ABOUT GYM</a></li>
    <li><a href="#">CLASS SCHEDULES</a></li>
    <li><a href="#">TRAINER PROFILES</a></li>
    <li><a href="#">GYM PHILOSOPHY</a></li>
  </ul>

  <p class="intro"><strong>Tallow</strong> - lorem ipsum dolor sit amet, consectetur adipiscing elit. Cras eu nisl fermentum, sollicitudin ex et, feugiat tellus. Proin dictum dolor sed nisi vehicula hendrerit. Aliquam maximus egestas tortor, ut bibendum mauris vestibulum sit.</p>

  <div class="pill pill-eco">
    <svg width="44" height="44" viewBox="0 0 44 44" fill="none" stroke="#fff" stroke-width="4" stroke-linejoin="round">
      <path d="M22 3 L30 11 M22 3 L14 11"/><path d="M41 22 L33 30 M41 22 L33 14"/>
      <path d="M22 41 L14 33 M22 41 L30 33"/><path d="M3 22 L11 14 M3 22 L11 30"/>
    </svg>
    <div>
      <h2>Fully ecological gym</h2>
      <p>The decor and lighting room made of recycled<br>materials and do not damage the environment.</p>
    </div>
  </div>

  <div class="pill pill-body">
    <svg width="48" height="40" viewBox="0 0 48 40" fill="#fff">
      <rect x="2" y="10" width="6" height="18" rx="2"/><rect x="40" y="10" width="6" height="18" rx="2"/>
      <rect x="8" y="16" width="32" height="6"/><rect x="16" y="8" width="16" height="22" rx="4"/>
      <rect x="18" y="32" width="12" height="7" rx="2"/>
    </svg>
    <div>
      <h2>No fitness equipment,<br>just exercises and body</h2>
      <p>Our body is the most ideal tool for training.</p>
    </div>
  </div>

  <div class="feature feature-rank">
    <svg width="48" height="40" viewBox="0 0 48 40" fill="none" stroke="#fff" stroke-width="3">
      <circle cx="24" cy="18" r="14"/><path d="M21 12 L25 10 V26" stroke-linecap="round"/>
      <path d="M4 20 Q6 34 20 38 M44 20 Q42 34 28 38"/>
    </svg>
    <p>Now we are working with some of the best and<br>most recognized in the world</p>
  </div>

  <div class="feature feature-social">
    <svg width="44" height="40" viewBox="0 0 44 40" fill="#fff">
      <circle cx="10" cy="10" r="6"/><circle cx="34" cy="10" r="6"/><circle cx="22" cy="13" r="7"/>
      <path d="M0 28 Q0 18 10 18 Q16 18 18 22 L12 30 Z"/><path d="M44 28 Q44 18 34 18 Q28 18 26 22 L32 30 Z"/>
      <path d="M10 38 Q10 22 22 22 Q34 22 34 38 Z"/>
    </svg>
    <p>Gym is more of a social hub where people come to exercise,<br>have fun, hang out and socialize for several hours</p>
  </div>

  <div class="divider"></div>

  <footer class="footer">
    <p class="copyright">© 2013-2016 TALLOW SL.<br>All rights reserved.</p>
    <div class="address">
      <svg width="10" height="14" viewBox="0 0 10 14"><path d="M5 0 A5 5 0 0 1 10 5 C10 9 5 14 5 14 C5 14 0 9 0 5 A5 5 0 0 1 5 0 Z" fill="#fff"/><circle cx="5" cy="5" r="2" fill="#0792cd"/></svg>
      <p>Unit 12, Cedarline Works - Harbour Loop Rd, Marisol<br>Trade District 2 - Dubai - United Arab Emirates</p>
    </div>
    <ul class="social">
      <li aria-label="Social link 1"></li>
      <li aria-label="Social link 2"></li>
      <li aria-label="Social link 3"></li>
      <li aria-label="Social link 4"></li>
    </ul>
  </footer>
</div>
</body>
</html>
```